Corvanta512 Business Card Redesign

I want to create a design for brand new business cards, I need something exceptional for clear plastic business card design. Please do not submit without it being on a clear design. Photos of the various logo versions attached.

```html
<!DOCTYPE html>
<html lang="en">
<head>
<meta charset="UTF-8">
<title>Corvanta512 Business Card</title>
<link href="https://fonts.googleapis.com/css2?family=Archivo:wght@400;500;700&display=swap" rel="stylesheet">
<style>
  :root {
    --page-bg: #e4e5e7;
    --card-top: #f4f5f6;
    --card-bottom: #e9ebee;
    --gold: #a97f3c;
    --gold-light: #c9a25a;
    --navy: #233862;
    --navy-dark: #1a2a4a;
    --ink: #3b3f47;
    --ink-soft: #4a4e55;
    --white: #ffffff;
  }
  * { margin: 0; padding: 0; box-sizing: border-box; }
  html, body {
    width: 1200px;
    height: 804px;
    overflow: hidden;
    background: var(--page-bg);
    font-family: "Archivo", Arial, sans-serif;
  }
  .card {
    position: absolute;
    left: 100px;
    top: 106px;
    width: 1000px;
    height: 592px;
    border-radius: 26px;
    overflow: hidden;
    background: linear-gradient(160deg, var(--card-top) 0%, #eef0f2 55%, var(--card-bottom) 100%);
    border: 1px solid rgba(255,255,255,0.8);
    box-shadow: 0 18px 40px rgba(30,40,60,0.18), inset 0 0 0 1px rgba(180,186,196,0.35);
  }
  .brand {
    position: absolute;
    left: 0;
    width: 100%;
    top: 60px;
    display: flex;
    flex-direction: column;
    align-items: center;
    gap: 22px;
  }
  .brand-mark {
    width: 120px;
    height: 120px;
    border-radius: 50%;
    background: var(--gold);
  }
  .brand-name {
    font-size: 40px;
    font-weight: 700;
    color: var(--gold);
    letter-spacing: 1px;
  }
  .person {
    position: absolute;
    left: 0;
    top: 296px;
  }
  .person-name-band {
    position: relative;
    width: 310px;
    height: 34px;
    background: linear-gradient(90deg, var(--gold) 0%, var(--gold-light) 50%, var(--gold) 100%);
    clip-path: polygon(0 0, 100% 0, 97% 100%, 0 100%);
    padding-left: 42px;
    display: flex;
    align-items: center;
  }
  .person-name {
    font-size: 22px;
    font-weight: 700;
    color: var(--white);
    letter-spacing: 1.5px;
  }
  .person-slash {
    position: absolute;
    left: 312px;
    top: 0;
    width: 10px;
    height: 34px;
    background: var(--navy);
    clip-path: polygon(60% 0, 100% 0, 40% 100%, 0 100%);
  }
  .person-role {
    margin-top: 8px;
    padding-left: 42px;
    font-size: 21px;
    font-weight: 400;
    color: var(--ink);
    letter-spacing: 2px;
  }
  .contact {
    position: absolute;
    display: flex;
    align-items: center;
    gap: 18px;
    font-size: 21px;
    font-weight: 500;
    color: var(--ink-soft);
    letter-spacing: 2px;
  }
  .contact svg { width: 30px; height: 30px; flex: none; }
  .contact-mobile { left: 136px; top: 408px; }
  .contact-phone { left: 136px; top: 469px; }
  .contact-email { left: 452px; top: 408px; }
  .contact-web { left: 452px; top: 470px; }
  .address-band {
    position: absolute;
    left: 0;
    bottom: 0;
    width: 100%;
    height: 46px;
    background: linear-gradient(90deg, var(--navy-dark) 0%, var(--navy) 100%);
    display: flex;
    align-items: center;
    padding-left: 124px;
    gap: 16px;
    color: #e6e9ef;
    font-size: 21px;
    font-weight: 500;
    letter-spacing: 2px;
  }
  .address-band svg { width: 26px; height: 32px; }
</style>
</head>
<body>
  <div class="card">
    <div class="brand">
      <div class="brand-mark"></div>
      <div class="brand-name">Corvanta512</div>
    </div>

    <div class="person">
      <div class="person-name-band"><span class="person-name">Name Here</span></div>
      <div class="person-slash"></div>
      <div class="person-role">Ceo</div>
    </div>

    <div class="contact contact-mobile">
      <svg viewBox="0 0 30 30" fill="none" stroke="#a97f3c" stroke-width="2">
        <rect x="9" y="3" width="12" height="24" rx="2"/>
        <circle cx="15" cy="23" r="1" fill="#a97f3c"/>
      </svg>
      <span>123-456-7890</span>
    </div>

    <div class="contact contact-phone">
      <svg viewBox="0 0 30 30" fill="none" stroke="#a97f3c" stroke-width="2" stroke-linejoin="round">
        <path d="M8 4l5 5-3 3c1.5 3.5 4.5 6.5 8 8l3-3 5 5-3 4C13 25 5 17 4 7z"/>
      </svg>
      <span>123-456-7890</span>
    </div>

    <div class="contact contact-email">
      <svg viewBox="0 0 30 30" fill="none" stroke="#a97f3c" stroke-width="2" stroke-linejoin="round">
        <rect x="3" y="7" width="24" height="16"/>
        <path d="M3 7l12 10 12-10M3 23l9-8M27 23l-9-8"/>
      </svg>
      <span>hello@corvanta512.com</span>
    </div>

    <div class="contact contact-web">
      <svg viewBox="0 0 30 30" fill="none" stroke="#a97f3c" stroke-width="2">
        <circle cx="15" cy="15" r="12"/>
        <ellipse cx="15" cy="15" rx="5" ry="12"/>
        <path d="M3 15h24M5 9h20M5 21h20"/>
      </svg>
      <span>www.corvanta512.com</span>
    </div>

    <div class="address-band">
      <svg viewBox="0 0 26 32" fill="none" stroke="#c9ced8" stroke-width="2">
        <path d="M13 27C8 20 5 15 5 11a8 8 0 0116 0c0 4-3 9-8 16z"/>
        <circle cx="13" cy="11" r="3"/>
        <ellipse cx="13" cy="28" rx="8" ry="2.5"/>
      </svg>
      <span>Address. 48 Lindell Row, Harbor City</span>
    </div>
  </div>
</body>
</html>
```